brixtane motor oil

I would like to inform you that our new motor oil brand brixtane will be divided into three categories:
Brixtane high performance Full Synthetic
0w20 ,5w30 ,0w16,5w20
with massage.
Maximum Protection, Ultimate Performance.brixtane quendor
--------------------------------
brixtane quendor Synthetic Blend
10w40,5w30,5w20
with massage
The perfect combination of durability and efficiency
-------------------------------
brixtane gelvoria transmission fluid
ATF III
with massage
proven to maximize transmission life

```html
<!DOCTYPE html>
<html lang="en">
<head>
<meta charset="utf-8">
<title>brixtane motor oil – label range</title>
<link rel="stylesheet" href="https://fonts.googleapis.com/css2?family=Arimo:wght@400&family=Exo+2:ital,wght@0,700;1,600;1,700;1,800;1,900&display=swap">
<style>
  :root {
    --page: #ffffff;
    --frame: #dddddd;
    --dim-line: #222222;
    --dim-ext: #d4d4d4;
    --dim-ink: #111111;
    --red-bright: #f2432f;
    --red-mid: #c0182c;
    --red-deep: #5c0a12;
    --blue-bright: #2a65ad;
    --blue-mid: #1b4a8e;
    --blue-deep: #0f2456;
    --atf-bright: #b8141c;
    --atf-deep: #4a060c;
    --ink-light: #ffffff;
  }
  * { box-sizing: border-box; margin: 0; padding: 0; }
  html, body { width: 1200px; height: 927px; overflow: hidden; background: var(--page); }
  .canvas {
    position: relative; width: 1200px; height: 927px;
    font-family: "Exo 2", sans-serif; color: var(--ink-light);
  }
  .sheet {
    position: absolute; left: 21px; top: 161px; width: 1158px; height: 605px;
    border: 1px solid var(--frame);
  }
  .dimensions { position: absolute; left: 0; top: 0; width: 1200px; height: 927px; }
  .dimensions .ext { stroke: var(--dim-ext); stroke-width: 0.6; }
  .dimensions .dim { stroke: var(--dim-line); stroke-width: 0.6; }
  .dim-value {
    position: absolute; transform: translate(-50%, -50%);
    font-family: "Arimo", sans-serif; font-size: 13px; line-height: 1;
    color: var(--dim-ink); background: var(--page); padding: 2px 3px;
  }

  .label {
    position: absolute; display: flex; flex-direction: column;
    align-items: center; text-align: center; overflow: hidden;
  }
  .label--synthetic {
    left: 137px; top: 327px; width: 192px; height: 276px; padding-top: 58px;
    clip-path: polygon(0 40px, 100% 0, 100% 100%, 0 100%);
    background: radial-gradient(circle at 35% 22%, var(--red-bright), var(--red-mid) 45%, var(--red-deep) 100%);
  }
  .label--blend {
    left: 542px; top: 363px; width: 184px; height: 244px; padding-top: 58px;
    clip-path: polygon(0 44px, 100% 0, 100% 100%, 0 100%);
    background: linear-gradient(160deg, var(--blue-bright), var(--blue-mid) 50%, var(--blue-deep));
  }
  .label--atf {
    left: 928px; top: 434px; width: 125px; height: 176px; padding-top: 36px;
    clip-path: polygon(0 29px, 100% 0, 100% 100%, 0 100%);
    background: linear-gradient(165deg, var(--atf-bright) 40%, var(--atf-deep));
  }
  .brand { font-weight: 700; font-style: normal; letter-spacing: -0.5px; line-height: 1; }
  .range { font-weight: 900; font-style: italic; line-height: 1; }
  .subline { font-weight: 600; font-style: italic; letter-spacing: 1px; line-height: 1.1; }
  .grade { font-weight: 900; font-style: italic; line-height: 1; }
  .message { font-weight: 800; font-style: italic; line-height: 1.3; }

  .label--synthetic .brand { font-size: 40px; }
  .label--synthetic .range { font-size: 19px; margin-top: 1px; }
  .label--synthetic .range-top { font-size: 28px; margin-top: 12px; }
  .label--synthetic .subline { font-size: 14px; margin-top: 3px; }
  .label--synthetic .grade { font-size: 36px; margin-top: 5px; }
  .label--synthetic .message { font-size: 10.5px; margin-top: 12px; }

  .label--blend .brand { font-size: 38px; }
  .label--blend .range { font-size: 22px; margin-top: 12px; }
  .label--blend .subline { font-size: 13px; margin-top: 2px; }
  .label--blend .grade { font-size: 34px; margin-top: 10px; }
  .label--blend .message { font-size: 9.5px; margin-top: 12px; }

  .label--atf .brand { font-size: 25px; }
  .label--atf .range { font-size: 15px; margin-top: 12px; }
  .label--atf .subline { font-size: 8px; font-weight: 700; margin-top: 2px; letter-spacing: 0.4px; }
  .label--atf .grade { font-size: 23px; margin-top: 7px; }
  .label--atf .message { font-size: 6.5px; margin-top: 9px; }

  .seal {
    position: absolute; left: 162px; top: 206px; width: 24px; height: 24px;
    border: 2px solid var(--red-mid); border-radius: 50%;
  }
</style>
</head>
<body>
<main class="canvas">
  <div class="sheet"></div>

  <svg class="dimensions" viewBox="0 0 1200 927" aria-hidden="true">
    <defs>
      <marker id="arrow" viewBox="0 0 10 4" refX="10" refY="2" markerWidth="10" markerHeight="4" orient="auto-start-reverse" markerUnits="userSpaceOnUse">
        <path d="M0 0 L10 2 L0 4 Z" fill="#222"/>
      </marker>
    </defs>
    <!-- full synthetic -->
    <line class="ext" x1="78" y1="371" x2="137" y2="371"/>
    <line class="ext" x1="78" y1="603" x2="137" y2="603"/>
    <line class="ext" x1="329" y1="327" x2="440" y2="327"/>
    <line class="ext" x1="329" y1="603" x2="440" y2="603"/>
    <line class="ext" x1="137" y1="610" x2="137" y2="672"/>
    <line class="ext" x1="329" y1="610" x2="329" y2="672"/>
    <line class="dim" x1="83" y1="371" x2="83" y2="603" marker-start="url(#arrow)" marker-end="url(#arrow)"/>
    <line class="dim" x1="435" y1="327" x2="435" y2="603" marker-start="url(#arrow)" marker-end="url(#arrow)"/>
    <line class="dim" x1="137" y1="668" x2="329" y2="668" marker-start="url(#arrow)" marker-end="url(#arrow)"/>
    <!-- synthetic blend -->
    <line class="ext" x1="485" y1="407" x2="542" y2="407"/>
    <line class="ext" x1="485" y1="604" x2="542" y2="604"/>
    <line class="ext" x1="726" y1="363" x2="840" y2="363"/>
    <line class="ext" x1="726" y1="604" x2="840" y2="604"/>
    <line class="ext" x1="543" y1="612" x2="543" y2="673"/>
    <line class="ext" x1="726" y1="612" x2="726" y2="673"/>
    <line class="dim" x1="490" y1="407" x2="490" y2="604" marker-start="url(#arrow)" marker-end="url(#arrow)"/>
    <line class="dim" x1="835" y1="363" x2="835" y2="604" marker-start="url(#arrow)" marker-end="url(#arrow)"/>
    <line class="dim" x1="543" y1="669" x2="726" y2="669" marker-start="url(#arrow)" marker-end="url(#arrow)"/>
    <!-- transmission fluid -->
    <line class="ext" x1="882" y1="463" x2="928" y2="463"/>
    <line class="ext" x1="882" y1="609" x2="928" y2="609"/>
    <line class="ext" x1="1053" y1="434" x2="1110" y2="434"/>
    <line class="ext" x1="1053" y1="609" x2="1110" y2="609"/>
    <line class="ext" x1="928" y1="615" x2="928" y2="674"/>
    <line class="ext" x1="1053" y1="615" x2="1053" y2="674"/>
    <line class="dim" x1="886" y1="463" x2="886" y2="609" marker-start="url(#arrow)" marker-end="url(#arrow)"/>
    <line class="dim" x1="1105" y1="434" x2="1105" y2="609" marker-start="url(#arrow)" marker-end="url(#arrow)"/>
    <line class="dim" x1="928" y1="670" x2="1053" y2="670" marker-start="url(#arrow)" marker-end="url(#arrow)"/>
  </svg>

  <span class="dim-value" style="left:83px; top:487px;">171.67</span>
  <span class="dim-value" style="left:435px; top:450px;">204.18</span>
  <span class="dim-value" style="left:221px; top:668px;">141.43</span>
  <span class="dim-value" style="left:490px; top:477px;">146.21</span>
  <span class="dim-value" style="left:835px; top:484px;">177.35</span>
  <span class="dim-value" style="left:630px; top:669px;">135.45</span>
  <span class="dim-value" style="left:886px; top:530px;">108.20</span>
  <span class="dim-value" style="left:1105px; top:519px;">129.63</span>
  <span class="dim-value" style="left:990px; top:670px;">92.58</span>

  <section class="label label--synthetic">
    <p class="brand">brixtane</p>
    <p class="range range-top">HIGH</p>
    <p class="range">PERFORMANCE</p>
    <p class="subline">FULL SYNTHETIC</p>
    <p class="grade">0W-20</p>
    <p class="message">MAXIMUM PROTECTION,<br>ULTIMATE PERFORMANCE</p>
    <span class="seal" aria-hidden="true"></span>
  </section>

  <section class="label label--blend">
    <p class="brand">brixtane</p>
    <p class="range">QUENDOR</p>
    <p class="subline">SYNTHETIC BLEND</p>
    <p class="grade">10W-40</p>
    <p class="message">THE PERFECT COMBINATION<br>OF DURABILITY AND EFFICIENCY</p>
  </section>

  <section class="label label--atf">
    <p class="brand">brixtane</p>
    <p class="range">GELVORIA</p>
    <p class="subline">TRANSMISSION FLUID</p>
    <p class="grade">ATF III</p>
    <p class="message">PROVEN TO MAXIMIZE<br>TRANSMISSION LIFE</p>
  </section>
</main>
</body>
</html>
```